Boutique Recruiting Firm Needs Eye-Catching Business Cards (and potentially new logo)!

I run a recruiting company in Charleston, South Carolina. I have a ton of networking events coming up and need business cards to grab potential clients attention.

I currently have a logo but if you want to try and recreate the logo to something more modern I am open to that. If you do decide to create a new logo please submit the business card with the old logo and the new one.

Staffing Under Blue Lanterns, LLC is the name of my company. I create videos to my clients and candidates which allows me to standout from my competition so I would like a business card (and possibly new logo) to do the same.

I do not specialize in any one industry of recruiting.

```html
<!DOCTYPE html>
<html lang="en">
<head>
<meta charset="utf-8">
<title>Staffing Under Blue Lanterns, LLC – Business Card</title>
<link rel="stylesheet" href="https://fonts.googleapis.com/css2?family=Roboto:wght@400;500;700&display=swap">
<style>
  :root {
    --ink: #4a4a4a;
    --ink-soft: #555555;
    --brand-blue: #0b6aa8;
    --paper: #ffffff;
    --edge: #d9d9d9;
  }
  * { box-sizing: border-box; margin: 0; padding: 0; }
  html, body { width: 1200px; height: 705px; overflow: hidden; background: var(--paper); }
  .card {
    position: relative;
    width: 1200px;
    height: 705px;
    background: var(--paper);
    border: 1px solid var(--edge);
    font-family: "Roboto", Arial, sans-serif;
    color: var(--ink);
  }
  .brand {
    position: absolute;
    left: 86px;
    top: 110px;
    width: 356px;
    height: 486px;
    display: flex;
    flex-direction: column;
    justify-content: center;
    gap: 26px;
  }
  .brand-square {
    width: 64px;
    height: 64px;
    background: var(--brand-blue);
  }
  .brand-name {
    font-weight: 700;
    font-size: 50px;
    line-height: 1.08;
    color: var(--brand-blue);
    text-transform: uppercase;
  }
  .divider {
    position: absolute;
    left: 533px;
    top: 108px;
    width: 2px;
    height: 488px;
    background: var(--ink);
  }
  .person {
    position: absolute;
    left: 598px;
    top: 102px;
  }
  .person-name {
    font-weight: 700;
    font-size: 41px;
    line-height: 1.1;
    color: var(--ink);
  }
  .person-role {
    margin-top: 10px;
    font-size: 26px;
    font-weight: 400;
    color: var(--ink-soft);
  }
  .contacts {
    position: absolute;
    left: 595px;
    top: 350px;
    list-style: none;
  }
  .contact {
    display: flex;
    align-items: center;
    height: 50.5px;
    font-size: 28px;
    letter-spacing: 0.4px;
    color: var(--ink-soft);
  }
  .contact-icon {
    width: 38px;
    height: 38px;
    margin-right: 35px;
    flex: none;
  }
</style>
</head>
<body>
  <div class="card">
    <div class="brand" aria-label="Staffing Under Blue Lanterns, LLC">
      <div class="brand-square"></div>
      <div class="brand-name">Staffing Under Blue Lanterns, LLC</div>
    </div>

    <div class="divider"></div>

    <div class="person">
      <h1 class="person-name">Dev Malhotra</h1>
      <p class="person-role">Managing Director</p>
    </div>

    <ul class="contacts">
      <li class="contact">
        <svg class="contact-icon" viewBox="0 0 38 38" aria-hidden="true">
          <path d="M19 3a11 11 0 0 0-11 11c0 8 11 21 11 21s11-13 11-21A11 11 0 0 0 19 3z" fill="var(--ink)"/>
          <circle cx="19" cy="14" r="4.5" fill="var(--paper)"/>
        </svg>
        <span>12 Lantern Row, King Street</span>
      </li>
      <li class="contact">
        <svg class="contact-icon" viewBox="0 0 38 38" aria-hidden="true">
          <circle cx="19" cy="19" r="16" fill="none" stroke="var(--ink)" stroke-width="2"/>
          <path d="M13 10l4 0 2 5-3 2c1 3 3 5 6 6l2-3 5 2 0 4c-1 1-3 2-5 1-6-2-11-7-13-13-0-2 1-3 2-4z" fill="none" stroke="var(--ink)" stroke-width="2" stroke-linejoin="round"/>
        </svg>
        <span>+1 843 555 0142</span>
      </li>
      <li class="contact">
        <svg class="contact-icon" viewBox="0 0 38 38" aria-hidden="true">
          <rect x="3" y="8" width="32" height="22" fill="none" stroke="var(--ink)" stroke-width="2"/>
          <path d="M3 8l16 13 16-13M3 30l12-11M35 30l-12-11" fill="none" stroke="var(--ink)" stroke-width="2"/>
        </svg>
        <span>hello@bluelanterns.com</span>
      </li>
      <li class="contact">
        <svg class="contact-icon" viewBox="0 0 38 38" aria-hidden="true">
          <g fill="none" stroke="var(--ink)" stroke-width="2">
            <circle cx="19" cy="19" r="16"/>
            <ellipse cx="19" cy="19" rx="7" ry="16"/>
            <path d="M3 19h32M6 11h26M6 27h26"/>
          </g>
        </svg>
        <span>www.staffingbluelanterns.com</span>
      </li>
      <li class="contact">
        <svg class="contact-icon" viewBox="0 0 38 38" aria-hidden="true">
          <rect x="4" y="4" width="30" height="30" rx="5" fill="var(--ink)"/>
        </svg>
        <span>linkhub.com/bluelanternsllc</span>
      </li>
    </ul>
  </div>
</body>
</html>
```